Young Accounting firm needing a captivating business card

We need a business card design that forces the person to look at the card because its either gold foil, plastic, or lettering pop up etc. We already have a logo with a specific gold color and we need to make it pop. We are an accounting firm. I need the words" accounting, payroll, licenses, audits, taxes" somewhere on the business card so as to describe what we do- preferably on the side where the logo is at.

Industry/Entity Type

Accounting

Contact Information for Business Card

Address 48276 9th Ave S Ste 305, Maple Bend, OR 97117
Business Phone (503)418-2096
Fax (503)418-2157
Office Cell Phone (503)586-7319

Font styles to use
Serif

Colors
85abd2

Requirements
Must have
• It should state
• "Accounting" "Taxes" "Audits" "Licenses" "Payroll"
Nice to have
• Matte with gold foil, different textures, With Either a textured ivory background or gray blue slate background
Should not have
• colorful colors

```html
<!DOCTYPE html>
<html lang="en">
<head>
<meta charset="utf-8">
<title>NPTaxworks Business Card</title>
<link href="https://fonts.googleapis.com/css2?family=Arimo:wght@400;500&display=swap" rel="stylesheet">
<style>
  :root {
    --backdrop: #1c1f23;
    --slate-light: #5d6877;
    --slate-mid: #4a5666;
    --slate-deep: #34404f;
    --gold: #c9a227;
    --ink-light: #f2f2f2;
  }
  * { margin: 0; padding: 0; box-sizing: border-box; }
  html, body {
    width: 1200px;
    height: 1200px;
    overflow: hidden;
    background: var(--backdrop);
    font-family: "Arimo", Arial, sans-serif;
  }
  .sheet {
    width: 1200px;
    height: 1200px;
    display: flex;
    flex-direction: column;
    align-items: center;
    justify-content: center;
    gap: 34px;
  }
  .card {
    position: relative;
    width: 960px;
    height: 549px;
    background: linear-gradient(180deg,
      var(--slate-light) 0%,
      var(--slate-mid) 22%,
      var(--slate-deep) 45%,
      var(--slate-mid) 75%,
      var(--slate-light) 100%);
    box-shadow: 0 10px 30px rgba(0,0,0,0.5);
  }
  .brand {
    display: flex;
    align-items: center;
    gap: 12px;
    color: var(--gold);
    font-weight: 400;
    letter-spacing: 0.5px;
  }
  .brand-mark { background: var(--gold); }

  /* contact side */
  .card--contact .brand {
    position: absolute;
    top: 58px;
    right: 64px;
    font-size: 40px;
  }
  .card--contact .brand-mark { width: 26px; height: 26px; }
  .contact-list {
    position: absolute;
    left: 64px;
    bottom: 56px;
    list-style: none;
    color: var(--ink-light);
    font-size: 24px;
    line-height: 1.35;
  }
  .contact-item {
    display: flex;
    align-items: flex-start;
    gap: 12px;
  }
  .contact-icon {
    width: 22px;
    height: 22px;
    margin-top: 4px;
    flex: none;
  }

  /* logo side */
  .card--front {
    display: flex;
    flex-direction: column;
    align-items: center;
    justify-content: center;
    gap: 34px;
  }
  .card--front .brand {
    font-size: 74px;
    gap: 18px;
  }
  .card--front .brand-mark { width: 44px; height: 44px; }
  .services {
    display: flex;
    list-style: none;
    gap: 14px;
    color: var(--ink-light);
    font-size: 25px;
  }
  .service {
    display: flex;
    align-items: center;
    gap: 7px;
  }
  .service::before {
    content: "";
    width: 12px;
    height: 12px;
    border-radius: 50%;
    background: var(--gold);
  }
</style>
</head>
<body>
<main class="sheet">
  <section class="card card--contact" aria-label="Contact side">
    <div class="brand"><span class="brand-mark"></span><span class="brand-name">NPTaxworks</span></div>
    <ul class="contact-list">
      <li class="contact-item">
        <svg class="contact-icon" viewBox="0 0 24 24" aria-hidden="true"><circle cx="12" cy="12" r="12" fill="#c9a227"/><path d="M8 6.5c.6-.4 1.3-.3 1.6.3l1 1.9c.3.5.1 1.1-.3 1.4l-.8.6c.6 1.3 1.6 2.3 2.8 2.9l.6-.8c.3-.4.9-.6 1.4-.3l1.9 1c.6.3.7 1 .3 1.6l-.8 1c-.5.6-1.3.8-2 .5-3.2-1.3-5.6-3.7-6.8-6.8-.3-.7-.1-1.5.5-2z" fill="#34404f"/></svg>
        <span>(503)418-2096</span>
      </li>
      <li class="contact-item">
        <svg class="contact-icon" viewBox="0 0 24 24" aria-hidden="true"><rect x="3" y="9" width="18" height="10" rx="1.5" fill="#c9a227"/><rect x="7" y="4" width="10" height="6" fill="#c9a227"/><rect x="7" y="13" width="10" height="2" fill="#34404f"/></svg>
        <span>(503)418-2157</span>
      </li>
      <li class="contact-item">
        <svg class="contact-icon" viewBox="0 0 24 24" aria-hidden="true"><circle cx="12" cy="12" r="12" fill="#c9a227"/><path d="M8 6.5c.6-.4 1.3-.3 1.6.3l1 1.9c.3.5.1 1.1-.3 1.4l-.8.6c.6 1.3 1.6 2.3 2.8 2.9l.6-.8c.3-.4.9-.6 1.4-.3l1.9 1c.6.3.7 1 .3 1.6l-.8 1c-.5.6-1.3.8-2 .5-3.2-1.3-5.6-3.7-6.8-6.8-.3-.7-.1-1.5.5-2z" fill="#34404f"/></svg>
        <span>(503)586-7319</span>
      </li>
      <li class="contact-item">
        <svg class="contact-icon" viewBox="0 0 24 24" aria-hidden="true"><path d="M12 1a7 7 0 0 0-7 7c0 5 7 12 7 12s7-7 7-12a7 7 0 0 0-7-7z" fill="#c9a227"/><circle cx="12" cy="8" r="2.6" fill="#34404f"/><path d="M4 22h16" stroke="#c9a227" stroke-width="1.6"/></svg>
        <span>48276 9th Ave S Ste 305<br>Maple Bend , OR 97117</span>
      </li>
    </ul>
  </section>

  <section class="card card--front" aria-label="Logo side">
    <div class="brand"><span class="brand-mark"></span><span class="brand-name">NPTaxworks</span></div>
    <ul class="services">
      <li class="service">Accounting</li>
      <li class="service">Taxes</li>
      <li class="service">Audits</li>
      <li class="service">Licenses</li>
      <li class="service">Payroll</li>
    </ul>
  </section>
</main>
</body>
</html>
```